Window cleaning company in need of leaflet design

Family run business requires leaflet design.
Our company uses water fed pole with pure water which is what the leaflet needs to emphasise on (include a background picture of a water fed pole cleaning a window.)

other services we offer which i would like to include are:
• facia/soffit cleaning.
• Conservatory cleans.
• Gutter clearing which is performed by a gutter vacuum pictures of gutters before and after clean are provided to every customer if they require.
• pressure washing

uploaded company logo to be included on leaflet.
number to include is 07715264389
email address is Rtglasscare@mailbay.test
would also like a facebook symbol included to show we are on social media.
Thank you

Font styles to use
Serif
Sans Serif

Colors
00a990
33a6d7
3276b5
3277b5
34a7d8
87cfc6
33b8a4
cfdfed
85acd3

Requirements
Must have
• We use traditional and water fed pole methods of cleaning. So those hard to reach or awkward to clean windows are not a problem. No need for ladders.

Our water fed pole system uses 100% pure water. This is water that has been de-ironised and de-mineralised to ensue it’s perfectly pure for a spot free finish.

• fully insured

• regular and reliable service
• one off cleans available

Call dean on 07715264389 for a free quote

```html
<!DOCTYPE html>
<html lang="en">
<head>
<meta charset="utf-8">
<title>R.T Glass Care – Leaflet</title>
<link rel="stylesheet" href="https://fonts.googleapis.com/css2?family=Montserrat:wght@500;600;700;800&family=Open+Sans:wght@400;600;700&display=swap">
<style>
:root{
  --teal:#00a990;
  --teal-soft:#33b8a4;
  --teal-pale:#87cfc6;
  --sky:#33a6d7;
  --blue:#3276b5;
  --ice:#cfdfed;
  --mist:#85acd3;
  --ink:#3c4650;
  --grey:#8a949c;
  --paper:#ffffff;
}
*{margin:0;padding:0;box-sizing:border-box}
html,body{width:1200px;height:2232px;overflow:hidden;background:var(--paper)}
body{font-family:"Open Sans",Arial,sans-serif;color:var(--ink);position:relative}
.brand{position:absolute;top:120px;left:0;width:1200px;display:flex;justify-content:center;align-items:center;gap:22px}
.brand-mark{width:28px;height:28px;background:var(--teal);border-radius:50%}
.brand-name{font-family:"Montserrat",Arial,sans-serif;font-weight:600;font-size:72px;color:var(--blue);letter-spacing:1px;white-space:nowrap}
.hero{position:absolute;top:240px;left:0;width:1200px;height:1230px}
.services{position:absolute;left:70px;top:1500px;width:500px}
.section-title{font-family:"Montserrat",Arial,sans-serif;font-weight:800;font-size:40px;color:var(--teal);letter-spacing:1px;text-transform:uppercase;margin-bottom:22px}
.service-list{list-style:none}
.service-list li{font-size:30px;line-height:52px;padding-left:34px;position:relative}
.service-list li::before{content:"";position:absolute;left:0;top:20px;width:13px;height:13px;background:var(--teal);border-radius:50%}
.gutter-shots{display:flex;gap:24px;margin-top:34px}
.gutter-shot{width:220px;height:140px;border:4px solid var(--teal);border-radius:6px}
.gutter-shot.before{background:linear-gradient(135deg,#7d7a72,#b9b3a6)}
.gutter-shot.after{background:linear-gradient(135deg,#c7ccd0,#eef1f3)}
.about{position:absolute;left:620px;top:1490px;width:520px}
.about-box{border-left:6px solid var(--teal-pale);padding-left:26px}
.about-box p{font-size:25px;line-height:37px;margin-bottom:20px}
.tick-list{list-style:none;margin-top:26px;padding-left:32px}
.tick-list li{font-size:27px;line-height:50px;display:flex;align-items:center;gap:16px}
.tick-list svg{flex:none}
.contact-rule{position:absolute;left:0;top:1995px;width:1200px;border-top:3px solid var(--teal-pale)}
.quote-bar{position:absolute;left:70px;top:2030px;background:var(--teal);color:#fff;font-size:25px;font-weight:600;padding:10px 26px;border-radius:4px;white-space:nowrap}
.phone{position:absolute;left:70px;top:2100px;display:flex;align-items:center;gap:16px;font-family:"Montserrat",Arial,sans-serif;font-weight:800;font-size:56px;color:var(--teal)}
.email-row{position:absolute;right:60px;top:2040px;display:flex;align-items:center;gap:14px;font-size:26px;color:var(--blue);font-weight:600;white-space:nowrap}
.email-row .icon-dot{width:40px;height:40px;border-radius:50%;background:var(--teal)}
.footer-line{position:absolute;left:0;bottom:0;width:1200px;height:26px;background:var(--teal)}
</style>
</head>
<body>
<header class="brand">
  <span class="brand-mark"></span>
  <span class="brand-name">R.T Glass Care</span>
</header>

<svg class="hero" viewBox="0 0 1200 1230" xmlns="http://www.w3.org/2000/svg">
  <defs>
    <clipPath id="heroClip">
      <path d="M0 330 L230 70 L420 250 L600 40 L800 230 L980 70 L1200 300 L1200 1080 Q600 1240 0 1080 Z"/>
    </clipPath>
    <linearGradient id="heroFill" x1="0" y1="0" x2="1" y2="1">
      <stop offset="0" stop-color="#dfe9ee"/>
      <stop offset="0.5" stop-color="#b8d6e4"/>
      <stop offset="1" stop-color="#8fc9b9"/>
    </linearGradient>
  </defs>
  <g clip-path="url(#heroClip)">
    <rect width="1200" height="1230" fill="url(#heroFill)" role="img" aria-label="Photo of a smiling cleaner holding a basket of cleaning sprays and cloths beside a bright window"/>
  </g>
  <path d="M0 330 L230 70 L420 250 L600 40 L800 230 L980 70 L1200 300" fill="none" stroke="#00a990" stroke-width="22"/>
  <path d="M0 380 L230 125 L420 305 L600 95 L800 285 L980 125 L1200 350" fill="none" stroke="#87cfc6" stroke-width="6"/>
  <path d="M0 1080 Q600 1240 1200 1080 L1200 1230 L0 1230 Z" fill="#ffffff"/>
  <path d="M0 1080 Q600 1240 1200 1080" fill="none" stroke="#00a990" stroke-width="16"/>
  <path d="M0 1110 Q600 1265 1200 1110" fill="none" stroke="#87cfc6" stroke-width="6"/>
</svg>

<section class="services">
  <h2 class="section-title">Services we offer</h2>
  <ul class="service-list">
    <li>Fascia/soffit cleaning</li>
    <li>Conservatory cleans</li>
    <li>Gutter clearing</li>
    <li>Pressure washing</li>
  </ul>
  <div class="gutter-shots">
    <div class="gutter-shot before" role="img" aria-label="Gutter before vacuum clearing"></div>
    <div class="gutter-shot after" role="img" aria-label="Gutter after vacuum clearing"></div>
  </div>
</section>

<section class="about">
  <div class="about-box">
    <p>We use traditional and water fed pole methods of cleaning. So those hard to reach or awkward to clean windows are not a problem. No need for ladders.</p>
    <p>Our water fed pole system uses 100% pure water. This is water that has been de-ionised and de-mineralised to ensure it's perfectly pure for a spot free finish.</p>
  </div>
  <ul class="tick-list">
    <li><svg width="26" height="26" viewBox="0 0 26 26"><path d="M3 14 L10 21 L23 5" fill="none" stroke="#00a990" stroke-width="4"/></svg>Fully insured</li>
    <li><svg width="26" height="26" viewBox="0 0 26 26"><path d="M3 14 L10 21 L23 5" fill="none" stroke="#00a990" stroke-width="4"/></svg>Regular and reliable service</li>
    <li><svg width="26" height="26" viewBox="0 0 26 26"><path d="M3 14 L10 21 L23 5" fill="none" stroke="#00a990" stroke-width="4"/></svg>One off cleans available</li>
  </ul>
</section>

<div class="contact-rule"></div>
<div class="quote-bar">Call dean on 07715264389 for a free quote</div>
<div class="phone">
  <svg width="50" height="50" viewBox="0 0 50 50"><circle cx="25" cy="25" r="24" fill="#00a990"/><path d="M17 13 L22 13 L24 20 L21 22 Q24 28 28 29 L30 26 L37 28 L37 33 Q36 37 32 37 Q16 35 13 18 Q13 13 17 13 Z" fill="#fff"/></svg>
  <span>07715264389</span>
</div>
<div class="email-row">
  <svg width="40" height="40" viewBox="0 0 40 40"><circle cx="20" cy="20" r="19" fill="#00a990"/><rect x="10" y="13" width="20" height="14" fill="none" stroke="#fff" stroke-width="2.5"/><path d="M10 13 L20 22 L30 13" fill="none" stroke="#fff" stroke-width="2.5"/></svg>
  <span>Rtglasscare@mailbay.test</span>
  <span class="icon-dot"></span>
  <span class="icon-dot"></span>
</div>
<div class="footer-line"></div>
</body>
</html>
```